Professional and creatice Life Coach - Business Card design

I just relaunched my website and now i a need a correspoonding business card for my task as life coach. My website is www.dlorvan.net as reference. The compass is kind of a symbol for my work, as I help people navigate through their challenging phases in life. The business card should be colorful, but not too playful as I also adress business people. So it sould be creative, but professional (also to suport my other business as Management Consultant)

Target Market(s)

People who want to get teir problems resolved, in business, partnership and other personal realms

Industry/Entity Type

Life Coaching

Contact Information for Business Card

Front side should include Name, Phone number, Email, Website and address

Font styles to use
Sans Serif

Colors
add136

Requirements
Must have
• "Mag. Benedikt Haufmoll" -> Name
"Energetische Praxis" -> Jobtitle (describing my profession as life coach)
colours and style should match my website www.dlorvan.net
Nice to have
• a compass as a symbol

```html
<!DOCTYPE html>
<html lang="de">
<head>
<meta charset="utf-8">
<title>Haufmoll – Visitenkarte</title>
<link rel="stylesheet" href="https://fonts.googleapis.com/css2?family=Ubuntu:wght@400;500;700&display=swap">
<style>
  :root {
    --stage: #2b2e33;
    --card: #1b1b1c;
    --card-edge: #262627;
    --lime: #add136;
    --white: #f2f2f2;
    --grey: #7d7d80;
  }
  * { margin: 0; padding: 0; box-sizing: border-box; }
  html, body { width: 1200px; height: 900px; overflow: hidden; background: var(--stage); }
  body { position: relative; font-family: "Ubuntu", "Segoe UI", sans-serif; }

  .card {
    position: absolute;
    left: 320px;
    width: 560px;
    height: 320px;
    background: var(--card);
    border-radius: 18px;
    box-shadow: 0 0 0 1px var(--card-edge), 0 14px 30px rgba(0,0,0,.45);
    overflow: hidden;
  }
  .card--front { top: 100px; }
  .card--back { top: 480px; }

  .identity { position: absolute; left: 44px; top: 88px; }
  .identity__name { color: var(--lime); font-size: 30px; font-weight: 500; letter-spacing: .2px; }
  .identity__role { color: var(--white); font-size: 16px; margin-top: 4px; }

  .divider {
    position: absolute; left: 250px; top: 168px; width: 310px; height: 4px;
    background: linear-gradient(90deg, var(--lime) 0%, var(--lime) 55%, rgba(173,209,54,0) 100%);
  }

  .brand { position: absolute; display: flex; align-items: center; gap: 10px; }
  .brand__dot { border-radius: 50%; border: 3px solid currentColor; }
  .brand__name { font-weight: 500; }
  .card--front .brand { right: 40px; top: 56px; color: var(--lime); }
  .card--front .brand__dot { width: 30px; height: 30px; }
  .card--front .brand__name { font-size: 22px; }

  .contacts { position: absolute; left: 262px; top: 192px; list-style: none; }
  .contacts li {
    display: flex; align-items: center; gap: 12px;
    color: var(--white); font-size: 14px; font-weight: 500; height: 26px;
  }
  .contacts svg { width: 14px; height: 14px; fill: none; stroke: var(--lime); stroke-width: 1.6; }

  .card--back .brand { left: 50%; top: 110px; transform: translateX(-50%); color: var(--grey); }
  .card--back .brand__dot { width: 36px; height: 36px; }
  .card--back .brand__name { font-size: 30px; }
  .back__web { position: absolute; left: 0; right: 0; top: 196px; text-align: center; color: var(--grey); font-size: 14px; }
</style>
</head>
<body>
  <section class="card card--front">
    <div class="identity">
      <h1 class="identity__name">Mag. Benedikt Haufmoll</h1>
      <p class="identity__role">Energetische Praxis</p>
    </div>
    <div class="divider"></div>
    <div class="brand"><span class="brand__dot"></span><span class="brand__name">Haufmoll</span></div>
    <ul class="contacts">
      <li><svg viewBox="0 0 16 16"><path d="M4 1.5l2.5 3-1.5 2a8 8 0 0 0 4.5 4.5l2-1.5 3 2.5-1.5 2.5C7 14.5 1.5 9 1.5 3z"/></svg>+43 660 4718392</li>
      <li><svg viewBox="0 0 16 16"><rect x="1.5" y="3.5" width="13" height="9" rx="1"/><path d="M1.5 4l6.5 5 6.5-5"/></svg>benedikt@haufmoll.one</li>
      <li><svg viewBox="0 0 16 16"><circle cx="8" cy="8" r="6.5"/><path d="M1.5 8h13M8 1.5c-3 3.5-3 9.5 0 13M8 1.5c3 3.5 3 9.5 0 13"/></svg>www.dlorvan.net</li>
      <li><svg viewBox="0 0 16 16"><path d="M8 15s5-5.2 5-8.5A5 5 0 0 0 3 6.5C3 9.8 8 15 8 15z"/><circle cx="8" cy="6.5" r="1.8"/></svg>Lindenstieg 9, 5071 Wolfsau, Austria</li>
    </ul>
  </section>

  <section class="card card--back">
    <div class="brand"><span class="brand__dot"></span><span class="brand__name">Haufmoll</span></div>
    <p class="back__web">www.dlorvan.net</p>
  </section>
</body>
</html>
```